Corinne Dabney Interiors business cards

We need a DOUBLE SIDED business card design that is simple, elegant and modern. We are a rapidly growing Interior Design Firm, and our brand colours are blush pink, navy, and antique gold, so we require some or all of these colours to be used. The final design should portray elegance, simplicity, and have a modern feel. We have upload inspiration photos that have the feel we're looking for.

Industry/Entity Type

Interior Design

Contact Information for Business Card

Contact information and LOGO

Colors
EB3D1F
EC4F4E
F09395
F8D3D4
FCEDEE

Requirements
Must have
• Navy, the right shade of blush pink, and antique gold

```html
<!DOCTYPE html>
<html lang="en">
<head>
<meta charset="utf-8">
<title>Corinne Dabney Interiors – Business Cards</title>
<link href="https://fonts.googleapis.com/css2?family=Open+Sans:wght@400;700;800&display=swap" rel="stylesheet">
<style>
  :root {
    --navy: #21285a;
    --coral: #eb5150;
    --gold: #9c7c4f;
    --blush: #fdeced;
    --page: #ffffff;
  }
  * { margin: 0; padding: 0; box-sizing: border-box; }
  html, body {
    width: 1200px; height: 900px; overflow: hidden;
    background: var(--page);
    font-family: "Open Sans", Arial, sans-serif;
  }
  .canvas { position: relative; width: 1200px; height: 900px; }
  .card {
    position: absolute; left: 247px; width: 675px; height: 405px;
    box-shadow: 4px 6px 10px rgba(0,0,0,0.35);
    overflow: hidden;
  }
  .card--front { top: 24px; }
  .card--back { top: 471px; }
  .card__art { position: absolute; inset: 0; width: 100%; height: 100%; display: block; }
  .fill-gold { fill: var(--gold); }
  .fill-navy { fill: var(--navy); }
  .fill-coral { fill: var(--coral); }
  .fill-blush { fill: var(--blush); }

  .brand {
    position: absolute; display: flex; align-items: center; gap: 10px;
    color: var(--gold); font-weight: 400; white-space: nowrap;
  }
  .brand__square { width: 14px; height: 14px; background: var(--navy); flex: none; }
  .brand--front { left: 0; right: 0; top: 188px; justify-content: center; font-size: 27px; }
  .brand--back { left: 26px; width: 305px; top: 190px; justify-content: center; font-size: 21px; }

  .divider {
    position: absolute; left: 336px; top: 114px; width: 2px; height: 177px;
    background: var(--navy);
  }
  .identity { position: absolute; left: 357px; top: 88px; color: var(--navy); }
  .identity__name { font-size: 28px; font-weight: 800; line-height: 1.1; letter-spacing: 0.2px; }
  .identity__role { font-size: 15.5px; font-weight: 700; line-height: 1.2; }

  .contacts {
    position: absolute; left: 357px; top: 197px; list-style: none;
    color: var(--navy); font-size: 16px;
  }
  .contacts__item { display: flex; align-items: center; gap: 7px; height: 26px; }
  .contacts__icon { width: 19px; height: 19px; flex: none; }
</style>
</head>
<body>
<div class="canvas">

  <section class="card card--front" aria-label="Card front">
    <svg class="card__art" viewBox="0 0 1125 675" preserveAspectRatio="none" aria-hidden="true">
      <rect class="fill-gold" width="1125" height="675"/>
      <polygon class="fill-navy" points="0,20 551,113 0,208"/>
      <polygon class="fill-coral" points="1125,18 578,113 1125,208"/>
      <polygon class="fill-blush" points="0,208 551,113 578,113 1125,208 1125,469 578,563 551,563 0,469"/>
      <polygon class="fill-navy" points="0,469 551,563 0,657"/>
      <polygon class="fill-coral" points="1125,469 578,563 1125,657"/>
    </svg>
    <div class="brand brand--front"><span class="brand__square"></span>Corinne Dabney Interiors</div>
  </section>

  <section class="card card--back" aria-label="Card back">
    <svg class="card__art" viewBox="0 0 1125 675" preserveAspectRatio="none" aria-hidden="true">
      <rect class="fill-gold" width="1125" height="675"/>
      <polygon class="fill-navy" points="0,61 545,95 0,130"/>
      <polygon class="fill-coral" points="1125,61 575,95 1125,130"/>
      <polygon class="fill-blush" points="0,130 545,95 575,95 1125,130 1125,546 575,580 545,580 0,546"/>
      <polygon class="fill-navy" points="0,546 545,580 0,615"/>
      <polygon class="fill-coral" points="1125,546 575,580 1125,615"/>
    </svg>

    <div class="brand brand--back"><span class="brand__square"></span>Corinne Dabney Interiors</div>
    <div class="divider"></div>

    <div class="identity">
      <h1 class="identity__name">CORINNE DABNEY</h1>
      <p class="identity__role">PRINCIPAL DESIGNER</p>
    </div>

    <ul class="contacts">
      <li class="contacts__item">
        <svg class="contacts__icon" viewBox="0 0 24 24" aria-hidden="true">
          <path fill="#eb3d1f" d="M6.6 3.5 9 3l1.6 4.6-2 1.4a12 12 0 0 0 5.4 6.4l1.6-1.8 4.4 1.9-.6 2.5c-.3 1.2-1.5 2-2.8 1.8C9.8 18.9 4.5 13.5 3.6 6.8 3.4 5.3 4.8 3.9 6.6 3.5z"/>
          <path fill="none" stroke="#eb3d1f" stroke-width="1.5" stroke-linecap="round" d="M14 3.5a6.5 6.5 0 0 1 6.5 6.5M14 6.5a3.5 3.5 0 0 1 3.5 3.5"/>
        </svg>
        <span>905 555 0142</span>
      </li>
      <li class="contacts__item">
        <svg class="contacts__icon" viewBox="0 0 24 24" aria-hidden="true">
          <circle cx="12" cy="12" r="4" fill="none" stroke="#eb3d1f" stroke-width="2.6"/>
          <path fill="none" stroke="#eb3d1f" stroke-width="2.6" stroke-linecap="round" d="M16 9v4.5c0 2 2.8 2.3 3.8.3A9 9 0 1 0 16 20"/>
        </svg>
        <span>corinne@cdinteriorsinc.com</span>
      </li>
      <li class="contacts__item">
        <svg class="contacts__icon" viewBox="0 0 24 24" aria-hidden="true">
          <circle cx="12" cy="12" r="9.5" fill="#eb3d1f"/>
          <g fill="none" stroke="#fdeced" stroke-width="1.3">
            <ellipse cx="12" cy="12" rx="4" ry="9.5"/>
            <path d="M2.5 12h19M4 7h16M4 17h16M12 2.5v19"/>
          </g>
        </svg>
        <span>www.corinnedabneyinteriors.com</span>
      </li>
    </ul>
  </section>

</div>
</body>
</html>
```